Lumeva Botanics Natural baby skin and hair care

We need a look and feel for a line of baby care products. A lotion, Wash and baby oil. We already have an existing line of products and are now venturing into baby care. We want a natural look with "love, softness and a touch of earth and Africa'

Industry/Entity Type

Retail

Font styles to use
Script

Colors
fbed22
f78f20
9bcb3c

Requirements
Must have
• Natural elements
Should not have
• Red, Black abstract shapes

```html
<!DOCTYPE html>
<html lang="en">
<head>
<meta charset="utf-8">
<title>Lumeva Botanics Baby Care Labels</title>
<link href="https://fonts.googleapis.com/css2?family=Comfortaa:wght@400;600&display=swap" rel="stylesheet">
<style>
  :root {
    --sun: #fbed22;
    --clay: #f78f20;
    --ember: #f36c12;
    --leaf: #9bcb3c;
    --leaf-deep: #6fae1e;
    --olive: #8a8d52;
    --ink: #6b6b5a;
    --paper: #ffffff;
    --ground: #f2f5f4;
  }
  * { box-sizing: border-box; margin: 0; padding: 0; }
  html, body { width: 1200px; height: 1200px; overflow: hidden; }
  body {
    background: var(--ground);
    font-family: "Comfortaa", sans-serif;
    color: var(--ink);
    display: flex;
    align-items: flex-end;
    justify-content: center;
    gap: 48px;
    padding-bottom: 120px;
  }
  .label {
    background: var(--paper);
    border-radius: 6px;
    box-shadow: 0 2px 14px rgba(90, 100, 90, 0.12);
    display: flex;
    flex-direction: column;
    align-items: center;
    overflow: hidden;
    padding-top: 0;
  }
  .label--lotion, .label--wash { width: 320px; height: 860px; }
  .label--oil { width: 280px; height: 700px; }
  .stripes { width: 100%; display: block; }
  .brand {
    margin-top: 40px;
    display: flex;
    flex-direction: column;
    align-items: center;
    gap: 10px;
  }
  .brand__mark { width: 14px; height: 14px; background: var(--leaf); }
  .brand__name {
    font-weight: 400;
    font-size: 17px;
    letter-spacing: 3px;
    color: var(--ink);
    text-transform: uppercase;
    text-align: center;
  }
  .product-name {
    margin-top: 28px;
    font-size: 36px;
    font-weight: 600;
    color: var(--leaf-deep);
  }
  .label--oil .product-name { font-size: 30px; margin-top: 22px; }
  .descriptor {
    margin-top: 10px;
    font-size: 11px;
    line-height: 1.5;
    text-align: center;
    color: var(--ink);
  }
  .rule { width: 150px; height: 1px; background: var(--olive); margin: 8px 0; opacity: .6; }
  .claim { font-size: 14px; margin-top: 8px; }
  .benefits { display: flex; gap: 16px; margin-top: 18px; }
  .benefit { display: flex; flex-direction: column; align-items: center; gap: 4px; }
  .benefit svg { width: 40px; height: 40px; }
  .benefit span { font-size: 8px; font-weight: 600; text-transform: lowercase; }
  .benefit--nurture span { color: var(--leaf-deep); }
  .benefit--moisture span { color: var(--ember); }
  .benefit--soothe span { color: #e2c800; }
  .volume { font-size: 13px; margin-top: 18px; }
  .floral {
    margin-top: auto;
    width: 100%;
    height: 190px;
    background: linear-gradient(180deg, rgba(255,255,255,0) 0%, #eef0e2 45%, #e4e7cf 100%);
  }
  .label--oil .floral { height: 150px; }
</style>
</head>
<body>

<svg width="0" height="0" style="position:absolute">
  <defs>
    <symbol id="stripe-band" viewBox="0 0 320 130" preserveAspectRatio="none">
      <rect width="320" height="130" fill="var(--sun)"/>
      <rect y="0" width="320" height="8" fill="var(--leaf)"/>
      <rect y="14" width="320" height="10" fill="var(--sun)"/>
      <rect y="28" width="320" height="18" fill="var(--clay)"/>
      <rect y="50" width="320" height="5" fill="var(--leaf)"/>
      <rect y="60" width="320" height="12" fill="var(--sun)"/>
      <rect y="76" width="320" height="20" fill="var(--ember)"/>
      <rect y="100" width="320" height="6" fill="var(--leaf)"/>
      <rect y="110" width="320" height="12" fill="var(--clay)"/>
      <rect y="124" width="320" height="6" fill="var(--leaf)"/>
    </symbol>
    <symbol id="icon-nurture" viewBox="0 0 40 40">
      <circle cx="20" cy="20" r="19" fill="var(--leaf)"/>
      <path d="M11 28 C12 16 20 11 30 11 C29 21 23 28 11 28 Z M11 28 L24 16" fill="none" stroke="#fff" stroke-width="1.6"/>
    </symbol>
    <symbol id="icon-moisture" viewBox="0 0 40 40">
      <circle cx="20" cy="20" r="19" fill="var(--ember)"/>
      <path d="M20 9 C24 16 28 20 28 25 A8 8 0 0 1 12 25 C12 20 16 16 20 9 Z" fill="none" stroke="#fff" stroke-width="1.8"/>
    </symbol>
    <symbol id="icon-soothe" viewBox="0 0 40 40">
      <circle cx="20" cy="20" r="19" fill="var(--sun)"/>
      <path d="M9 17 q5.5-4 11 0 t11 0 M9 23 q5.5-4 11 0 t11 0" fill="none" stroke="#fff" stroke-width="2"/>
    </symbol>
    <symbol id="icon-protect" viewBox="0 0 40 40">
      <circle cx="20" cy="20" r="19" fill="var(--sun)"/>
      <path d="M20 9 L29 13 V20 C29 26 25 30 20 32 C15 30 11 26 11 20 V13 Z M15 20 l4 4 l7-8" fill="none" stroke="#fff" stroke-width="1.8"/>
    </symbol>
  </defs>
</svg>

<article class="label label--lotion">
  <svg class="stripes" height="130"><use href="#stripe-band" width="100%" height="130"/></svg>
  <div class="brand"><span class="brand__mark"></span><span class="brand__name">Lumeva Botanics</span></div>
  <h1 class="product-name">Baby Lotion</h1>
  <p class="descriptor">All Natural Shea Butter<br>&amp; Honey Baby Lotion</p>
  <div class="benefits">
    <div class="benefit benefit--nurture"><svg><use href="#icon-nurture"/></svg><span>nurture</span></div>
    <div class="benefit benefit--moisture"><svg><use href="#icon-moisture"/></svg><span>moisturise</span></div>
    <div class="benefit benefit--soothe"><svg><use href="#icon-soothe"/></svg><span>soothing</span></div>
  </div>
  <p class="volume">250ml/8oz.</p>
  <div class="floral" role="img" aria-label="Line drawing of flowers and leaves in olive green"></div>
</article>

<article class="label label--wash">
  <svg class="stripes" height="130"><use href="#stripe-band" width="100%" height="130"/></svg>
  <div class="brand"><span class="brand__mark"></span><span class="brand__name">Lumeva Botanics</span></div>
  <h1 class="product-name">Baby Wash</h1>
  <p class="descriptor">Natural Bath &amp; Body Wash</p>
  <span class="rule"></span>
  <p class="descriptor" style="margin-top:0">Shea Butter &amp; Chamomile</p>
  <div class="benefits">
    <div class="benefit benefit--nurture"><svg><use href="#icon-nurture"/></svg><span>nurture</span></div>
    <div class="benefit benefit--moisture"><svg><use href="#icon-moisture"/></svg><span>moisturise</span></div>
    <div class="benefit benefit--soothe"><svg><use href="#icon-soothe"/></svg><span>soothing</span></div>
  </div>
  <p class="volume">250ml/8oz.</p>
  <div class="floral" role="img" aria-label="Line drawing of flowers and leaves in olive green"></div>
</article>

<article class="label label--oil">
  <svg class="stripes" height="110"><use href="#stripe-band" width="100%" height="110"/></svg>
  <div class="brand"><span class="brand__mark"></span><span class="brand__name">Lumeva Botanics</span></div>
  <h1 class="product-name">Baby Oil</h1>
  <p class="descriptor">Pure Shea Oil &amp; Marula Oil<br>with Myrrh &amp; Frankincense</p>
  <p class="claim">100% Natural</p>
  <span class="rule"></span>
  <div class="benefits">
    <div class="benefit benefit--nurture"><svg><use href="#icon-nurture"/></svg><span>nurture</span></div>
    <div class="benefit benefit--moisture"><svg><use href="#icon-moisture"/></svg><span>moisturise</span></div>
    <div class="benefit benefit--soothe"><svg><use href="#icon-protect"/></svg><span>protect</span></div>
  </div>
  <div class="floral" role="img" aria-label="Line drawing of flowers and leaves in olive green"></div>
</article>

</body>
</html>
```